Dorvelan Swimming & Athletics Center

We need Business Card for a Athletics center
The logo frome the Uploaded Files ( b card fimal)
Οn one side of card we need the logo of company the Contact and the website:
1. Address:(Limassol, Cyprus 12-14 Stavrinelou str,Ano Trimeni,P.C. 4832)

2.Phone number: (+357) 25-704263

3. Mail: info@dorvelanfit.example

3. Website: www.dorvelanfit.example

Οn the other side of the card we need to write the sport of the company:

1. Artistic Gymnastics
2. Swimming
3. Gym - Fitness
4. Programs
5. Dancing
5.Tennis

From the Uploaded Files you can get the logo.In a logo is behind the black color which can be removed from logo.

Υou can use that color you want.
.
Updates

Industry/Entity Type

Business

Font styles to use
Decorative

Colors
0555a3
ffcf3e
3176b5
0692cd
add136
f04a50
000000
cfcfcf
9d9d9d

Requirements
Should not have
• photos with faces
• photo fro the Website:www.dorvelanfit.example

```html
<!DOCTYPE html>
<html lang="en">
<head>
<meta charset="utf-8">
<title>Dorvelan Swimming &amp; Athletics Center – Business Card</title>
<link rel="stylesheet" href="https://fonts.googleapis.com/css2?family=Roboto:wght@400;900&display=swap">
<style>
  :root {
    --stage: #3b3b3b;
    --card-dark: #161616;
    --card-light: #ffffff;
    --gold: #ffcf3e;
    --gold-deep: #f0902a;
    --gold-light: #fff08a;
    --navy: #1b2150;
    --text-light: #f2f2f2;
    --rule: #9d9d9d;
  }
  html, body {
    margin: 0;
    padding: 0;
    width: 1200px;
    height: 1000px;
    overflow: hidden;
    background: var(--stage);
    font-family: "Roboto", Arial, sans-serif;
  }
  .canvas {
    position: relative;
    width: 1200px;
    height: 1000px;
  }
  .card {
    position: absolute;
    left: 287px;
    width: 626px;
    height: 357px;
    overflow: hidden;
    box-shadow: 0 6px 18px rgba(0,0,0,0.45);
  }
  .card--front { top: 140px; background: var(--card-dark); }
  .card--back  { top: 531px; background: var(--card-light); height: 358px; }
  .card__band {
    position: absolute;
    left: 0; right: 0; bottom: 0;
    height: 16px;
    background: linear-gradient(90deg, var(--gold-deep) 0%, var(--gold) 30%, var(--gold-light) 50%, var(--gold) 70%, var(--gold-deep) 100%);
  }
  .brand {
    position: absolute;
    top: 78px;
    left: 0; right: 0;
    display: flex;
    align-items: center;
    justify-content: center;
    gap: 22px;
  }
  .brand__name {
    font-weight: 900;
    font-size: 54px;
    letter-spacing: 2px;
    color: var(--gold);
    line-height: 1;
  }
  .brand__mark {
    width: 74px;
    height: 74px;
    border-radius: 50%;
    background: var(--gold);
  }
  .contact {
    position: absolute;
    top: 198px;
    left: 0; right: 0;
    text-align: center;
    color: var(--text-light);
    font-size: 15px;
    line-height: 19px;
  }
  .contact p { margin: 0; }
  .contact__address { margin-bottom: 11px !important; }
  .contact__label { color: var(--gold); }
  .contact__sep { margin: 0 6px; }
  .back-brand {
    position: absolute;
    left: 130px;
    top: 112px;
    width: 152px;
    display: flex;
    flex-direction: column;
    align-items: center;
    gap: 12px;
  }
  .back-brand__mark {
    width: 76px;
    height: 76px;
    border-radius: 50%;
    background: var(--gold);
  }
  .back-brand__name {
    font-weight: 900;
    font-size: 25px;
    color: var(--navy);
    letter-spacing: 1px;
  }
  .divider {
    position: absolute;
    left: 301px;
    top: 120px;
    width: 2px;
    height: 125px;
    background: linear-gradient(180deg, rgba(157,157,157,0) 0%, var(--rule) 20%, var(--rule) 80%, rgba(157,157,157,0) 100%);
  }
  .sports {
    position: absolute;
    left: 328px;
    top: 119px;
    margin: 0;
    padding: 0;
    list-style: none;
    color: var(--navy);
    font-size: 16px;
    line-height: 22.5px;
  }
</style>
</head>
<body>
<main class="canvas">
  <section class="card card--front" aria-label="Business card front">
    <div class="brand">
      <span class="brand__name">DORVELAN</span>
      <span class="brand__mark" aria-hidden="true"></span>
    </div>
    <div class="contact">
      <p class="contact__address">Limassol, Cyprus 12-14 Stavrinelou str,<br>Ano Trimeni, P.C. 4832</p>
      <p><span class="contact__label">P</span> : (+357) 25-704263<span class="contact__sep">|</span><span class="contact__label">E</span> : info@dorvelanfit.example</p>
      <p>www.dorvelanfit.example</p>
    </div>
    <div class="card__band"></div>
  </section>

  <section class="card card--back" aria-label="Business card back">
    <div class="back-brand">
      <span class="back-brand__mark" aria-hidden="true"></span>
      <span class="back-brand__name">DORVELAN</span>
    </div>
    <div class="divider"></div>
    <ul class="sports">
      <li>1. Artistic Gymnastics</li>
      <li>2. Swimming</li>
      <li>3. Gym - Fitness</li>
      <li>4. Programs</li>
      <li>5. Dancing</li>
      <li>6.Tennis</li>
    </ul>
    <div class="card__band"></div>
  </section>
</main>
</body>
</html>
```